45 Flat Style Icons Needed

We are a real estate technology company that provides a couple different services to our users. I want the design to be both flat (colored) and have a solid color option (black). Winning designer will have opportunity for 3 much larger projects coming up.

Social User - This is a user that is actively communicating
Signal User - This is a user that is actively searching and viewing listings
Profiled User - This is a user that has registered for the service
Contact Information - This is a column header for user contact information
Visit Count - This is a column header to show how many times a visitor has viewed the website
Last Visit - This is a column header to show when the person visited the website last
Message Sent - This is a column header to show how many messages the user has sent to the visitor
Message Read - This is a column header to show how many messages have been read by the visitor
Listings Viewed - This is a column header to show how many real estate property listings the visitor has viewed
Searches Performed - This is a column header to show how many searches have been performed
Average Price - This is a column header to show what the average price the visitor is searching for
Listing Match - This is a column header to show if the visitor matches one of the users real estate listings
Lead Owner - This is a column header to show which user owns that lead
Shared Lead - This is a column header to show that the lead is being shared by multiple real estate agents
New Lead - This is an icon that is clicked to add a new lead by entering in contact information
New Report - This is an icon that is clicked to create a report on lead information
Share Lead - This is an icon that is clicked to share the lead with multiple real estate agents
Archive - This is an icon that is clicked to archive the lead
Lead Stream - This is like a plinkbook news feed
Lead Manager - This is like an address book
Harbor QLM - This is a real estate property search
Edit Website - This is the button people push to edit their Website
Tandem Reach - This is a social network posting system (post to multiple networks at once)
Admin Settings - This is just an account settings area
Advanced Settings - This is a super admin settings area to manage multiple accounts
New Leads - This is a notification area icon that shows when a new lead has been added (like plinkbook friend request)
Messages - This is a notification area icon that shows when a new message has come in (like plinkbook message)
Recommendations - This is an automatically generated recommendation (Think lightbulb)
Content Manager - This is a RSS Feed reader where people go to add content to their blog
Scheduled Posts - This is where people schedule plinkbook/tweets/blogs to post at a later date
Listings Manager - This is where people go to manage, add or remove real estate property listings
Post History - This is where people can see all previous social network posts
Order Content - This is where people go to purchase custom content for their website/blogs/tweets/plinkbook posts
Upgrade - This is where people go to upgrade their account
User Status - This is a column header that shows what stage the user is in
Stop Posting - This is an icon that is clicked to stop posting a certain real estate listing
Edit Lead - This is an icon that is clicked to change contact details of a lead
View Listing - This is an icon that is clicked to visit a real estate listing detail webpage
Edit This Post - This is an icon that is clicked to edit a social network post
Delete - This is an icon that is clicked to remove a social network post
Clock - This is an icon that shows what date and time something happened
Add Listing - This is an icon that is clicked to add a real estate property listing to the listing manager
Remove Listing - This is an icon that is clicked to remove a real estate property listing from the listing manager
Re-Use Post - This is an icon that is clicked to duplicate the social network post.
Updates

There are two designs that I have my eyes on. Thank you all for the hard work. I know that the payment is lower than most of you would like. Part of this projects low price is that i'll be hiring the designer direct for a few other jobs (if they'd like) I need to see a few things from everyone that remains in the contest. #1) The rest of the designs - I cannot choose someone without seeing all of the icons. #2) I need a colored version and a black & white version. Ultimately I will need these images to be scalable so when this is sent to me i'd like them in the following sizes as transparent .png's and an editable file format as well. 18x18 32x32 128x128 512x512

Industry/Entity Type

Real Estate

Requirements
Must have
• Multiple Colors throughout the icons.
The should have some basic depth - see example.

***THESE WILL NEED TO DISPLAY WELL AT 18x18px.

```html
<!DOCTYPE html>
<html lang="en">
<head>
<meta charset="utf-8">
<title>Lead Stat Icons</title>
<link href="https://fonts.googleapis.com/css2?family=Source+Sans+3:wght@400;700&display=swap" rel="stylesheet">
<style>
  :root {
    --page-bg: #ffffff;
    --stat-border: #5a5a5f;
    --stat-top: #ffffff;
    --stat-bottom: #d6d6dc;
    --rose: #dc1f5f;
    --plum: #9b1d5d;
    --violet: #652a93;
    --lilac: #b7a0d2;
    --lilac-deep: #a68ac6;
    --orange: #f5a31b;
    --orange-deep: #ef7d1a;
    --label: #777777;
  }
  html, body {
    margin: 0;
    padding: 0;
    overflow: hidden;
    background: var(--page-bg);
  }
  .canvas {
    position: relative;
    width: 1200px;
    height: 849px;
    overflow: hidden;
    background: var(--page-bg);
    font-family: "Source Sans 3", "Myriad Pro", Arial, sans-serif;
  }
  .stat {
    position: absolute;
    width: 257px;
  }
  .stat-box {
    position: relative;
    box-sizing: border-box;
    width: 257px;
    height: 48px;
    border: 1.5px solid var(--stat-border);
    border-radius: 6px;
    background: linear-gradient(to bottom, var(--stat-top) 0%, #ececf0 45%, var(--stat-bottom) 100%);
  }
  .stat-icon {
    position: absolute;
    left: 11px;
    top: 50%;
    transform: translateY(-50%);
    display: block;
  }
  .stat-value {
    position: absolute;
    right: 24px;
    top: 50%;
    transform: translateY(-50%);
    font-weight: 700;
    line-height: 1;
    white-space: nowrap;
  }
  .value-large { font-size: 38px; }
  .value-medium { font-size: 23px; }
  .value-small { font-size: 22px; }
  .rose { color: var(--rose); }
  .plum { color: var(--plum); }
  .violet { color: var(--violet); }
  .stat-label {
    position: absolute;
    left: 1px;
    font-size: 13.5px;
    color: var(--label);
    white-space: nowrap;
  }
</style>
</head>
<body>
<main class="canvas">

  <!-- Row 1 -->
  <section class="stat" style="left:152px; top:244px;">
    <div class="stat-box">
      <svg class="stat-icon" width="48" height="32" viewBox="0 0 48 32" aria-hidden="true">
        <rect x="1" y="1" width="46" height="30" rx="4" fill="var(--rose)"/>
        <path d="M3 4 L24 19 L45 4" fill="none" stroke="#fff" stroke-width="1.6"/>
        <path d="M3 29 L18 15 M45 29 L30 15" fill="none" stroke="#fff" stroke-width="1.4"/>
      </svg>
      <span class="stat-value value-large rose">41</span>
    </div>
    <span class="stat-label" style="top:55px;">Message sent</span>
  </section>

  <section class="stat" style="left:493px; top:244px;">
    <div class="stat-box">
      <svg class="stat-icon" width="42" height="40" viewBox="0 0 42 40" aria-hidden="true">
        <path d="M2 16 L21 2 L40 16 L40 37 Q40 39 38 39 L4 39 Q2 39 2 37 Z" fill="var(--rose)" stroke="#fff" stroke-width="1"/>
        <path d="M8 20 L8 9 L34 9 L34 20 L21 28 Z" fill="#fff"/>
        <path d="M3 17 L21 29 L39 17" fill="none" stroke="#fff" stroke-width="1.5"/>
        <path d="M3 38 L16 26 M39 38 L26 26" fill="none" stroke="#fff" stroke-width="1.3"/>
      </svg>
      <span class="stat-value value-large rose">38</span>
    </div>
    <span class="stat-label" style="top:55px;">Message read</span>
  </section>

  <section class="stat" style="left:826px; top:244px;">
    <div class="stat-box">
      <svg class="stat-icon" width="72" height="34" viewBox="0 0 72 34" aria-hidden="true" style="left:16px;">
        <g fill="var(--plum)">
          <path d="M2 2 L2 28 L8 22 L13 32 L17 30 L12 20 L20 20 Z"/>
          <path d="M26 2 L26 28 L32 22 L37 32 L41 30 L36 20 L44 20 Z"/>
          <path d="M50 2 L50 28 L56 22 L61 32 L65 30 L60 20 L68 20 Z"/>
        </g>
      </svg>
      <span class="stat-value value-large plum" style="right:15px;">4312</span>
    </div>
    <span class="stat-label" style="top:55px; left:11px;">visit count</span>
  </section>

  <!-- Row 2 -->
  <section class="stat" style="left:152px; top:396px;">
    <div class="stat-box">
      <svg class="stat-icon" width="66" height="32" viewBox="0 0 66 32" aria-hidden="true" style="left:3px;">
        <path d="M22 2 L66 2 L66 30 L22 30 L14 16 Z" fill="var(--rose)"/>
        <circle cx="24" cy="16" r="2.6" fill="#fff"/>
        <path d="M22 16 C10 10 2 12 2 17 C2 22 10 22 22 16" fill="none" stroke="var(--rose)" stroke-width="1.5"/>
      </svg>
      <span class="stat-value value-large rose">4.1</span>
    </div>
    <span class="stat-label" style="top:61px; left:5px;">average price</span>
  </section>

  <section class="stat" style="left:493px; top:396px;">
    <div class="stat-box">
      <svg class="stat-icon" width="48" height="44" viewBox="0 0 48 44" aria-hidden="true">
        <path d="M2 18 L20 2 L38 18" fill="none" stroke="var(--orange-deep)" stroke-width="3.5" stroke-linejoin="round"/>
        <path d="M6 18 L20 6 L34 18 L34 40 L6 40 Z" fill="var(--orange)"/>
        <circle cx="34" cy="31" r="11" fill="#fff"/>
        <circle cx="34" cy="31" r="8.5" fill="var(--orange)"/>
        <path d="M29.5 31 L33 34.5 L39 27.5" fill="none" stroke="#fff" stroke-width="2.4" stroke-linecap="round" stroke-linejoin="round"/>
      </svg>
      <span class="stat-value value-medium rose" style="right:15px;">match found</span>
    </div>
    <span class="stat-label" style="top:61px;">listing match</span>
  </section>

  <section class="stat" style="left:826px; top:396px;">
    <div class="stat-box">
      <svg class="stat-icon" width="24" height="34" viewBox="0 0 24 34" aria-hidden="true" style="left:17px;">
        <path d="M2 2 L2 28 L8 22 L13 32 L17 30 L12 20 L20 20 Z" fill="var(--plum)"/>
      </svg>
      <span class="stat-value value-small plum" style="right:16px;">2 June, Fri</span>
    </div>
    <span class="stat-label" style="top:55px; left:11px;">last visit</span>
  </section>

  <!-- Row 3 -->
  <section class="stat" style="left:291px; top:537px;">
    <div class="stat-box">
      <svg class="stat-icon" width="48" height="32" viewBox="0 0 48 32" aria-hidden="true" style="left:14px;">
        <rect x="2" y="2" width="32" height="28" rx="2" fill="var(--lilac)"/>
        <g fill="#fff">
          <rect x="8" y="7" width="3" height="3"/><rect x="14" y="7" width="16" height="3"/>
          <rect x="8" y="14" width="3" height="3"/><rect x="14" y="14" width="12" height="3"/>
          <rect x="8" y="21" width="3" height="3"/><rect x="14" y="21" width="10" height="3"/>
        </g>
        <path d="M22 20 Q33 10 44 20 Q33 30 22 20 Z" fill="#fff" stroke="var(--lilac)" stroke-width="1.8"/>
        <circle cx="33" cy="20" r="3.6" fill="var(--violet)"/>
      </svg>
      <span class="stat-value value-small violet" style="right:18px;">24</span>
    </div>
    <span class="stat-label" style="top:55px;">listings viewed</span>
  </section>

  <section class="stat" style="left:675px; top:533px;">
    <div class="stat-box">
      <svg class="stat-icon" width="38" height="38" viewBox="0 0 38 38" aria-hidden="true" style="left:16px;">
        <circle cx="19" cy="19" r="18" fill="var(--lilac-deep)" stroke="#fff" stroke-width="1.5"/>
        <circle cx="21" cy="16" r="6.5" fill="none" stroke="#fff" stroke-width="2.6"/>
        <path d="M16.5 20.5 L10 27" stroke="#fff" stroke-width="3.4" stroke-linecap="round"/>
      </svg>
      <span class="stat-value value-small violet" style="right:20px;">31</span>
    </div>
    <span class="stat-label" style="top:59px;">searches performed</span>
  </section>

</main>
</body>
</html>
```